BrixolaV

Hi, We are looking for a design Label for our Packaged Drinking Water. We want a label in rich color. The current Label is uploaded. We wish for a much brighter color rather than black. Our current label is in black. We have attached other company labels to give you idea. The Lomtra bottle image is also uploaded they use sticker for their bottle, front sticker contains name and back sticker's inner portion has graphics and the outer side has information we also open to that.
Industry/Entity Type
Packaged Drinking Water Bottle Brand
Look and feel
Each slider illustrates characteristics of the customer's brand and the style your logo design should communicate.

```html
<!DOCTYPE html>
<html lang="en">
<head>
<meta charset="utf-8">
<title>BrixolaV Packaged Drinking Water Labels</title>
<link href="https://fonts.googleapis.com/css2?family=Ubuntu:wght@300;400;700&display=swap" rel="stylesheet">
<style>
  :root {
    --canvas: #ffffff;
    --orange: #f25c05;
    --orange-line: #f7a13a;
    --label-white: #f7f7f7;
    --sky: #3ec6e0;
    --lime: #a8f01c;
    --teal: #14c9a6;
    --teal-dots: #9be8d6;
    --tag-orange: #f2581c;
    --shadow: rgba(0, 0, 0, 0.12);
  }
  * { box-sizing: border-box; margin: 0; padding: 0; }
  html, body {
    width: 1200px;
    height: 1056px;
    overflow: hidden;
    background: var(--canvas);
  }
  .canvas {
    position: relative;
    width: 1200px;
    height: 1056px;
    display: flex;
    justify-content: center;
    align-items: center;
    gap: 100px;
    font-family: "Ubuntu", sans-serif;
  }
  .label {
    position: relative;
    width: 440px;
    height: 570px;
    overflow: hidden;
    box-shadow: 0 6px 24px var(--shadow);
  }
  .label__top,
  .label__bottom {
    position: absolute;
    left: 0;
    width: 100%;
  }
  .label__top { top: 0; height: 56%; }
  .label__bottom { bottom: 0; height: 44%; }

  /* Orange edition */
  .label--orange .label__top { background: var(--orange); }
  .label--orange .label__bottom { background: var(--label-white); }
  .label--orange .label__pattern {
    position: absolute;
    top: 0; left: 0;
    width: 100%;
    height: 62%;
    background: linear-gradient(180deg, #f47a26 0%, var(--orange) 100%);
  }
  .label--orange .brand { color: #ffffff; }
  .label--orange .tagline { color: var(--sky); }

  /* Lime edition */
  .label--lime .label__top { background: var(--label-white); }
  .label--lime .label__bottom { background: var(--lime); }
  .label--lime .label__pattern {
    position: absolute;
    top: 30px;
    left: 10%;
    width: 80%;
    height: 300px;
    border-radius: 220px 220px 0 0;
    background: radial-gradient(circle at 50% 100%, var(--label-white) 0%, var(--label-white) 30%, var(--teal-dots) 55%, #d4f5ec 100%);
  }
  .label--lime .brand { color: var(--teal); }
  .label--lime .tagline { color: var(--tag-orange); }

  .brand {
    position: absolute;
    left: 0;
    width: 100%;
    top: 44%;
    display: flex;
    justify-content: center;
    align-items: center;
    gap: 14px;
    font-size: 66px;
    font-weight: 700;
    letter-spacing: 0.5px;
    line-height: 1;
  }
  .brand__mark {
    width: 18px;
    height: 18px;
    border-radius: 50%;
    background: currentColor;
  }
  .tagline {
    position: absolute;
    right: 44px;
    top: 73%;
    text-align: right;
    font-size: 28px;
    line-height: 1.12;
    text-transform: uppercase;
  }
  .tagline__light { font-weight: 300; display: block; }
  .tagline__bold { font-weight: 700; display: block; }
  .tagline__wide { font-weight: 300; display: block; letter-spacing: 4px; }
</style>
</head>
<body>
<main class="canvas">
  <section class="label label--orange">
    <div class="label__top">
      <div class="label__pattern" role="img" aria-label="Flowing wavy line pattern in light orange over the orange band"></div>
    </div>
    <div class="label__bottom"></div>
    <h1 class="brand"><span class="brand__mark"></span>BrixolaV</h1>
    <p class="tagline">
      <span class="tagline__light">Packaged</span>
      <span class="tagline__bold">Drinking</span>
      <span class="tagline__wide">Water</span>
    </p>
  </section>

  <section class="label label--lime">
    <div class="label__top">
      <div class="label__pattern" role="img" aria-label="Half-circle burst of small teal droplet marks"></div>
    </div>
    <div class="label__bottom"></div>
    <h2 class="brand"><span class="brand__mark"></span>BrixolaV</h2>
    <p class="tagline">
      <span class="tagline__light">Packaged</span>
      <span class="tagline__bold">Drinking</span>
      <span class="tagline__wide">Water</span>
    </p>
  </section>
</main>
</body>
</html>
```